Digital One Pager for Consulting Practice

I would like the essence of the content in my ppt consolidated into a one-pager. The one-pager will mainly be sent via email as a pdf and intended to excite and invite new clients and establish the credibility of my boutique high-end consulting firm. Infographics and symbols would be a plus. The target client should view the firm as providing premeir service. The client is getting a thought partner.

Target Market(s)

Large Medical Device Manufacturer Executives, Early-Stage Medical Device Manufacturer Executives, Partners at VC Firms

Industry/Entity Type

Medical Equipment

Colors
0355a3
f37122

Requirements
Must have
• Please match the color scheme in ppt. Please use the existing logo. I am very open to better graphics on the process. My photo does not need to be on the digital flyer. Hyper link to the website and email is needed.
Nice to have
• Infographics

```html
<!DOCTYPE html>
<html lang="en">
<head>
<meta charset="utf-8">
<title>Halvern Advisory – Regulatory Consulting</title>
<link href="https://fonts.googleapis.com/css2?family=Open+Sans:ital,wght@0,400;0,600;0,700;0,800;1,700;1,800&display=swap" rel="stylesheet">
<style>
:root{
  --blue:#0355a3;
  --navy:#0c1b33;
  --orange:#f37122;
  --ink:#2b2b2b;
  --grey-band:#e8e9eb;
  --panel:#f4f4f4;
  --badge-border:#b9bcc0;
}
*{margin:0;padding:0;box-sizing:border-box}
html,body{width:927px;height:1200px;overflow:hidden;background:#fff}
body{font-family:"Open Sans",Arial,sans-serif;color:var(--ink);position:relative}
.abs{position:absolute}
.backdrop{position:absolute;left:0;top:0}
.brand{left:37px;top:36px;color:var(--navy);font-weight:800;font-size:46px;line-height:48px;letter-spacing:6px}
.brand span{display:block;font-size:30px;letter-spacing:10px;line-height:34px}
.pillars{left:578px;top:0;width:311px;height:130px;background:var(--navy);border-radius:0 0 70px 70px;padding:18px 0 0 57px;list-style:none}
.pillars li{color:#fff;font-weight:800;font-style:italic;font-size:17.5px;line-height:23.5px}
.pillars li::before{content:"• "}
.heading{color:var(--blue);font-weight:700;font-size:26px;line-height:30px;display:flex;align-items:flex-start;gap:10px}
.heading::before{content:"";width:11px;height:11px;background:var(--orange);margin-top:10px;flex:none}
.heading.spaced{letter-spacing:2.5px}
.copy{font-size:13px;line-height:17.5px}
.copy p{margin-bottom:17.5px}
.copy .indent{padding-left:13px}
.svc-title{color:var(--orange);font-weight:700;font-size:13px;line-height:13px}
.svc-list{font-size:8.6px;line-height:13px;color:var(--ink)}
.step{width:124px;text-align:center;color:#fff;font-size:13px;line-height:17.5px;left:480px}
.partner-title{left:678px;top:524px;color:var(--blue);font-weight:700;font-size:27px;line-height:30px}
.badge{border:2px solid var(--badge-border);background:#fff;width:111px;height:52px}
.badge.navy{background:var(--navy)}
.badge.blue{background:var(--blue)}
.value{left:636px;top:1050px;width:291px;height:150px;background:var(--panel);padding:28px 0 0 42px}
.value h2{color:var(--navy);font-size:18px;font-weight:700;margin-bottom:13px}
.contact{display:flex;align-items:center;gap:6px;font-size:9.3px;line-height:19.5px}
.contact a{color:var(--ink);text-decoration:none}
.contact svg{width:10px;height:10px;flex:none}
.tag{color:#fff;font-weight:700;font-size:13px;display:flex;align-items:center;justify-content:center}
</style>
</head>
<body>

<svg class="backdrop" width="927" height="1200" viewBox="0 0 927 1200" aria-hidden="true">
  <path d="M760,176 L760,540 C760,800 560,975 320,980 C170,982 70,960 0,928" fill="none" stroke="var(--grey-band)" stroke-width="35"/>

  <!-- differentiators cycle -->
  <g fill="none" stroke-width="18">
    <path d="M171,684 A68,68 0 0 1 304,664" stroke="var(--orange)"/>
    <path d="M304,664 A68,68 0 0 1 239,752" stroke="var(--navy)"/>
    <path d="M239,752 A68,68 0 0 1 171,684" stroke="var(--blue)"/>
  </g>
  <polygon points="216,611 222,600 232,609" fill="var(--orange)"/>
  <polygon points="305,700 315,712 302,716" fill="var(--navy)"/>
  <polygon points="170,738 183,731 181,746" fill="var(--blue)"/>

  <!-- process column -->
  <rect x="480" y="540" width="124" height="496" fill="var(--navy)"/>
  <polygon points="480,664 604,664 542,704" fill="var(--orange)"/>
  <polygon points="480,788 604,788 542,828" fill="var(--orange)"/>
  <polygon points="480,912 604,912 542,952" fill="var(--orange)"/>
  <polygon points="480,1039 604,1039 542,1080" fill="#c9cbce"/>
  <polygon points="480,1036 604,1036 542,1076" fill="var(--orange)"/>

  <!-- step icons -->
  <circle cx="542" cy="601" r="26" fill="#fff"/>
  <path d="M532,590 l5,-3 4,8 -3,3 c2,5 5,8 9,10 l3,-3 8,4 -3,5 c-12,1 -24,-11 -23,-24z" fill="var(--navy)"/>
  <path d="M548,589 a9,9 0 0 1 8,8 M547,593 a5,5 0 0 1 5,5" stroke="var(--navy)" stroke-width="2" fill="none"/>

  <rect x="524" y="708" width="37" height="36" rx="3" fill="#fff"/>
  <path d="M524,744 L561,708" stroke="var(--navy)" stroke-width="2"/>
  <path d="M529,717 h10 M534,712 v10 M546,735 h10" stroke="var(--navy)" stroke-width="3"/>

  <path d="M542,834 c12,0 21,7 21,15 s-9,15 -21,15 c-3,0 -6,0 -9,-1 l-9,5 3,-8 c-4,-3 -6,-7 -6,-11 0,-8 9,-15 21,-15z" fill="#fff"/>
  <polygon points="553,826 563,843 543,843" fill="#fff" stroke="var(--navy)" stroke-width="1.5"/>
  <path d="M553,832 v6" stroke="var(--navy)" stroke-width="2"/>

  <path d="M525,956 h35 v26 h-28 l-7,7z" fill="#fff"/>
  <path d="M533,977 l14,-14 4,4 -14,14 h-4z M538,980 h16" fill="var(--navy)" stroke="var(--navy)" stroke-width="1.5"/>

  <!-- service rings -->
  <g fill="none" stroke="var(--orange)" stroke-width="3.5">
    <circle cx="74" cy="973" r="26"/>
    <circle cx="292" cy="973" r="26"/>
    <circle cx="74" cy="1077" r="26"/>
    <circle cx="292" cy="1077" r="26"/>
  </g>
  <g fill="var(--navy)">
    <path d="M72,960 l6,3 -6,12 -5,-3z M62,984 h24 v3 h-24z M66,980 a10,10 0 0 0 16,-8 l3,0 a13,13 0 0 1 -16,11z"/>
    <circle cx="284" cy="966" r="5"/><circle cx="300" cy="966" r="5"/>
    <path d="M277,985 a7,8 0 0 1 14,0z M293,985 a7,8 0 0 1 14,0z"/>
    <path d="M74,1064 l3,3 -3,3 -3,-3z M67,1072 h14 l-2,10 h-10z M63,1084 h22 v5 h-22z"/>
    <rect x="292" y="1064" width="16" height="11" fill="none" stroke="var(--navy)" stroke-width="2"/>
    <circle cx="283" cy="1070" r="3.5"/><path d="M279,1076 h8 v13 h-3 v-7 h-2 v7 h-3z M287,1077 l7,-4 1,2 -7,4z"/>
  </g>
</svg>

<div class="brand abs">HALVERN<span>ADVISORY</span></div>

<ul class="pillars abs">
  <li>Extensive Experience</li>
  <li>Efficient Process</li>
  <li>Valued Network</li>
</ul>

<h2 class="heading spaced abs" style="left:37px;top:190px">Experience</h2>
<div class="copy abs" style="left:37px;top:248px;width:360px">
  <p>•&nbsp; Over a decade&nbsp; @FDA (Former Deputy Division Director)</p>
  <p>•&nbsp; Expertise: Cardiovascular, Ophthalmology, General Hospital,<br>Infection Control, Dental, Anesthesia, Respiratory</p>
  <p>•&nbsp; Vice President Regulatory Affairs / Quality Assurance @Corvant<br>(Fortune 150 Company)</p>
  <div>•&nbsp; Initiated&nbsp; reorganization of department<br>•&nbsp; Led major compliance effort<br>•&nbsp; Successful FDA inspection (no observations)</div>
</div>

<h2 class="heading abs" style="left:470px;top:152px;letter-spacing:1px">Experience to Provide</h2>
<div class="copy abs" style="left:470px;top:211px;width:400px">
  <p>Executive Application Review</p>
  <div class="indent">•Examples include: Presubmission, IDE, 510(k) , 513(g), PMA,</div>
  <div>Refuse to Accept, Hold letter</div>
  <p class="indent">•Troubleshooting</p>
  <p>Strategic Advice &amp; Diligence to Investors</p>
  <div class="indent">•Validate &amp; Verify Founder Milestones<br>•Diligence portfolio company Regulatory and Quality systems</div>
</div>

<h2 class="heading abs" style="left:37px;top:521px">Differentiators</h2>
<div class="tag abs" style="left:133px;top:560px;width:106px;height:30px;background:var(--orange)">Experience</div>
<div class="tag abs" style="left:330px;top:730px;width:107px;height:28px;background:var(--navy)">Process</div>
<div class="tag abs" style="left:76px;top:756px;width:106px;height:28px;background:var(--blue)">Network</div>

<h2 class="heading abs" style="left:472px;top:466px">Efficient<br>Process</h2>
<div class="step abs" style="top:640px">Exploratory Call</div>
<div class="step abs" style="top:751px">Regulatory<br>Landscape</div>
<div class="step abs" style="top:873px">Problem<br>Statement</div>
<div class="step abs" style="top:994px">Review &amp; Align<br>on Deliverables</div>

<h2 class="partner-title abs">Valued Partner<br>Network</h2>
<div class="badge abs" style="left:678px;top:618px" role="img" aria-label="Partner badge"></div>
<div class="badge navy abs" style="left:778px;top:685px" role="img" aria-label="Partner badge"></div>
<div class="badge abs" style="left:678px;top:754px" role="img" aria-label="Partner badge"></div>
<div class="badge abs" style="left:778px;top:822px" role="img" aria-label="Partner badge"></div>
<div class="badge blue abs" style="left:678px;top:888px" role="img" aria-label="Partner badge"></div>
<div class="badge abs" style="left:778px;top:955px" role="img" aria-label="Partner badge"></div>

<h2 class="heading abs" style="left:37px;top:879px">Services</h2>
<div class="abs" style="left:106px;top:948px">
  <div class="svc-title">Regulatory Strategy</div>
  <div class="svc-list" style="margin-top:4px">•RAQA Organizational Structure<br>•Regulatory Pathway</div>
</div>
<div class="abs" style="left:324px;top:948px">
  <div class="svc-title">FDA Communications</div>
  <div class="svc-list" style="margin-top:4px">•Deficiency Response<br>•Application Review</div>
</div>
<div class="abs" style="left:106px;top:1045px">
  <div class="svc-title">Interim Executive<br>Leadership</div>
  <div class="svc-list" style="margin-top:8px">•Compliance Remediation<br>•Accelerated Product Registration</div>
</div>
<div class="abs" style="left:324px;top:1054px">
  <div class="svc-title">Training</div>
  <div class="svc-list" style="margin-top:5px">•FDA Communication<br>•MDR Reporting</div>
</div>

<div class="value abs">
  <h2>Halvern Advisory Value</h2>
  <div class="contact">
    <svg viewBox="0 0 10 10"><circle cx="5" cy="5" r="4.3" fill="none" stroke="var(--ink)" stroke-width="0.9"/><path d="M0.7,5h8.6M5,0.7c-2.4,2.4-2.4,6.2,0,8.6M5,0.7c2.4,2.4,2.4,6.2,0,8.6" fill="none" stroke="var(--ink)" stroke-width="0.8"/></svg>
    <a href="https://www.halvernadvisory.com">www.halvernadvisory.com</a>
  </div>
  <div class="contact">
    <svg viewBox="0 0 10 10"><path d="M1.5,1 l2,-0.5 1.3,2.6 -1,1 c0.6,1.4 1.6,2.4 3,3 l1,-1 2.6,1.3 -0.5,2 c-5,0 -8.4,-3.4 -8.4,-8.4z" fill="var(--ink)"/></svg>
    <span>555.014.2280</span>
  </div>
  <div class="contact">
    <svg viewBox="0 0 10 10"><rect x="0.5" y="2" width="9" height="6.5" fill="var(--ink)"/><path d="M0.8,2.3 L5,5.8 9.2,2.3" fill="none" stroke="#fff" stroke-width="0.8"/></svg>
    <a href="mailto:info@halvernadvisory.com">info@halvernadvisory.com</a>
  </div>
</div>

</body>
</html>
```